Label Sticker Design for Apothecary Brand

Hello! We are an independent grassroots business located in Ontario, Canada that specializes in making organic botanical and herbal skin care, tea, witchcraft and wellness products. We have been in business for 5 years and are looking to create a label sticker with one of our slogans for use in packaging.

Our brand is dark, herbal, witchy, and modern with old-world apothecary and vintage influences. We want a label that will be VERY clean, and easily explain what our product is, while conveying a sense of mysticism and magic, as well as a traditional apothecary vibe.

We have attached design inspiration to give you an idea of the style that we would like. Our demographic is hipster, current, (think finger tattoos, linen dresses, and organic groceries), and they care deeply about where we source our ingredients, and how we craft our product. We don't want an old-school sticker that looks like it should be on the shelves of a health food store. The design should be contemporary, upmarket, modern and clean, but evoke a strong sense of magic and self-care with wild gathered herbs and unusual wild flowers!

This will be used as a packaging sticker for our shipping boxes.

We look forward to your winning design!
Thank you very much.

Target Market(s)

20 - 50yr Female Demographic
Natural, bohemian, earthy, hipster and modern

Key Words: Minimalist Tattoos, Organic Skin Care, Bohemian, Witchy, Dark, Moody, Confident, Sustainable, Ethical,

PLEASE VIEW PHOTOS BEFORE SUBMITTING A DESIGN ;)

Industry/Entity Type

Skin Care Product

Font styles to use
Serif
Script

Colors
1b1b1b
5c5c5c
fbfbfb

Requirements
Must have
• Clean and Simple - Take a look at the photos we've posted!
• Black / greyscale (No color)
• Label sticker must be a rectangle (3" x 2")
• Very Modern with a touch of old-world
• We are open to a variety of font styles. Please see photo FONT in image files, or the images 'Bottle Inspiration'
• Please use the following text:
• Hollow Vesperine
• --------------------
• Crafted with Magic
• * Once your design is chosen and purchased, we will require the names of all fonts and sources of imagery used.
Nice to have
• A moody botanical graphic surrounding the text. Tangled wild, antique botanical illustrations. Not mandatory, but would be very nice.
Should not have
• Colour
• Messy or overly dramatic fonts
• Cartoon Imagery
• Leaf Motif
• Female Body Silhouettes
• Scroll or decorative borders.
• Butterflies, birds etc
• Actual pictures of witches
• Mandalas or Messy Graphics

```html
<!DOCTYPE html>
<html lang="en">
<head>
<meta charset="utf-8">
<title>Hollow Vesperine – Facial Balm Label</title>
<link href="https://fonts.googleapis.com/css2?family=Italianno&family=Courier+Prime:wght@400;700&display=swap" rel="stylesheet">
<style>
  :root {
    --page: #ffffff;
    --label-black: #1b1b1b;
    --botanical-tone: #2a2a2a;
    --band-grey: #5c5c5c;
    --band-text: #7a7a7a;
    --ink-light: #fbfbfb;
    --frame-line: #d6d6d6;
  }
  * { box-sizing: border-box; margin: 0; padding: 0; }
  html, body {
    width: 1200px; height: 1200px; overflow: hidden;
    background: var(--page);
  }
  .canvas { position: relative; width: 1200px; height: 1200px; }

  .label {
    position: absolute; left: 81px; top: 196px;
    width: 1036px; height: 691px;
    background: var(--label-black);
    overflow: hidden;
  }
  .botanical-backdrop {
    position: absolute; inset: 0 0 121px 0;
    background: radial-gradient(ellipse at 70% 40%, var(--botanical-tone) 0%, var(--label-black) 70%);
  }
  .frame {
    position: absolute; left: 38px; top: 38px;
    width: 966px; height: 560px;
    border: 3px solid var(--frame-line);
    border-bottom: none;
  }
  .brand-name {
    position: absolute; left: 0; right: 60px; top: 150px;
    text-align: center;
    font-family: "Italianno", cursive;
    font-size: 118px; line-height: 1;
    color: var(--ink-light);
  }
  .brand-rule {
    position: absolute; top: 320px; height: 3px;
    background: var(--ink-light);
  }
  .brand-rule--left { left: 199px; width: 210px; }
  .brand-rule--right { left: 489px; width: 342px; }
  .slogan-arc { position: absolute; left: 0; top: 0; }
  .slogan-arc text {
    font-family: "Courier Prime", monospace;
    font-size: 17px; fill: var(--ink-light); letter-spacing: 1px;
  }
  .product-line {
    position: absolute; left: 0; right: 60px; top: 450px;
    text-align: center;
    font-family: "Courier Prime", monospace;
    font-size: 21px; line-height: 33px; letter-spacing: 2px;
    color: var(--ink-light);
  }
  .info-band {
    position: absolute; left: 0; right: 0; bottom: 0; height: 121px;
    background: var(--band-grey);
    font-family: "Courier Prime", monospace;
    font-weight: 700; font-size: 20px; letter-spacing: 5px;
    color: var(--band-text);
  }
  .info-item {
    position: absolute; top: 0; height: 121px;
    display: flex; align-items: center; justify-content: center;
    text-align: center; line-height: 28px;
  }
  .info-item--volume { left: 100px; width: 120px; }
  .info-item--origin { left: 288px; width: 400px; }
  .info-item--organic { left: 790px; width: 150px; }
  .info-divider {
    position: absolute; top: 32px; width: 2px; height: 66px;
    background: var(--band-text);
  }
  .info-divider--first { left: 251px; }
  .info-divider--second { left: 748px; }
</style>
</head>
<body>
<div class="canvas">
  <section class="label">
    <div class="botanical-backdrop" role="img" aria-label="Faint antique wild flower illustration behind the label text"></div>
    <div class="frame"></div>

    <h1 class="brand-name">Hollow Vesperine</h1>
    <div class="brand-rule brand-rule--left"></div>
    <div class="brand-rule brand-rule--right"></div>

    <svg class="slogan-arc" width="1036" height="600" viewBox="0 0 1036 600" aria-label="Crafted with Magic.">
      <defs>
        <path id="slogan-path" d="M 785 142 A 105 105 0 0 1 935 275"/>
      </defs>
      <text><textPath href="#slogan-path">.Crafted with Magic.</textPath></text>
    </svg>

    <p class="product-line">FACIAL BALM WITH SACRED TULSI &amp;<br>MARSHMALLOW ROOT</p>

    <div class="info-band">
      <div class="info-item info-item--volume">50 ML</div>
      <div class="info-divider info-divider--first"></div>
      <div class="info-item info-item--origin">Authentic Product Of<br>Ontario</div>
      <div class="info-divider info-divider--second"></div>
      <div class="info-item info-item--organic">Organic</div>
    </div>
  </section>
</div>
</body>
</html>
```